I have a basketball training business combined with a strength training business. I train professio

I recently saw the cats that won the contest in the strength coach business card competition. I loved the design. I.want a card with my logo that calls attention to my clients as the card that won did to me. I would like to see if I could get a similar design. My logo is what I like although I must say I like the red and black design of the contest winner. perhaps if the smaller lettered portion of my logo coukd be separated from the larger KQT logo. It almost looks like 3M3. I like.the KQT Training and Development portion of it. I need help.

Training

```html
<!DOCTYPE html>
<html lang="en">
<head>
<meta charset="utf-8">
<title>KQT Training and Development – Business Card</title>
<link href="https://fonts.googleapis.com/css2?family=Open+Sans:wght@400;600;800&display=swap" rel="stylesheet">
<style>
  :root {
    --backdrop: #c9c9c9;
    --card-white: #ffffff;
    --brand-red: #e04a28;
    --charcoal: #2e2e2e;
    --logo-grey: #3a3a3a;
    --text-light: #ffffff;
  }
  * { margin: 0; padding: 0; box-sizing: border-box; }
  html, body { width: 1200px; height: 1000px; overflow: hidden; background: var(--backdrop); }
  .stage { position: relative; width: 1200px; height: 1000px; }
  .card {
    position: absolute; left: 150px; top: 240px; width: 900px; height: 520px;
    background: var(--card-white); overflow: hidden;
    box-shadow: 0 6px 18px rgba(0,0,0,.18);
  }
  .card-shapes { position: absolute; inset: 0; }
  .brand-name {
    position: absolute; left: 34px; top: 150px;
    display: flex; align-items: center; gap: 14px;
    font-family: "Open Sans", sans-serif; font-weight: 800; color: var(--logo-grey);
  }
  .brand-initials { font-size: 84px; line-height: 1; letter-spacing: -3px; }
  .brand-tagline { font-size: 31px; line-height: 1.0; text-transform: uppercase; letter-spacing: 3px; }
  .contact {
    position: absolute; font-family: "Open Sans", sans-serif; font-size: 19px;
    line-height: 1.25; color: var(--text-light);
  }
  .contact svg { position: absolute; left: -42px; top: 2px; }
  .contact-phone { left: 150px; top: 382px; }
  .contact-address { left: 150px; top: 448px; }
  .contact-web { left: 520px; top: 455px; }
  .name-badge {
    position: absolute; left: 440px; top: 360px; width: 400px; height: 82px;
    text-align: center; color: var(--text-light); font-family: "Open Sans", sans-serif;
    padding-top: 12px;
  }
  .person-name { font-size: 27px; font-weight: 400; line-height: 1.15; text-transform: uppercase; }
  .person-role { font-size: 18px; line-height: 1.2; }
</style>
</head>
<body>
<div class="stage">
  <div class="card">
    <svg class="card-shapes" width="900" height="520" viewBox="0 0 900 520" aria-hidden="true">
      <rect class="top-band" x="0" y="0" width="900" height="52" fill="var(--brand-red)"/>
      <path class="lower-panel" d="M0,318 C220,312 380,316 430,350 L840,350 C870,350 870,318 900,310 L900,520 L0,520 Z" fill="var(--charcoal)"/>
      <rect class="name-pill" x="440" y="360" width="400" height="82" rx="41" fill="var(--brand-red)"/>
    </svg>

    <div class="brand-name">
      <span class="brand-initials">KQT</span>
      <span class="brand-tagline">Training and<br>Development</span>
    </div>

    <div class="contact contact-phone">
      <svg width="26" height="26" viewBox="0 0 24 24" aria-hidden="true"><path fill="#fff" d="M6.6 10.8a15.1 15.1 0 0 0 6.6 6.6l2.2-2.2c.3-.3.7-.4 1-.2 1.1.4 2.3.6 3.6.6.6 0 1 .4 1 1V20c0 .6-.4 1-1 1A17 17 0 0 1 3 4c0-.6.4-1 1-1h3.5c.6 0 1 .4 1 1 0 1.3.2 2.5.6 3.6.1.3 0 .7-.2 1z"/></svg>
      +000 - 2468 - 1357<br>+000 - 8642 - 9753
    </div>

    <div class="contact contact-address">
      <svg width="30" height="26" viewBox="0 0 24 22" aria-hidden="true"><path fill="#fff" d="M12 1 0 11h3v10h7v-6h4v6h7V11h3z"/></svg>
      87 Avenue, Suite 4<br>Boston 10234
    </div>

    <div class="name-badge">
      <div class="person-name">Marcus Hale</div>
      <div class="person-role">Managing Director</div>
    </div>

    <div class="contact contact-web">
      <svg width="28" height="28" viewBox="0 0 24 24" aria-hidden="true" fill="none" stroke="#fff" stroke-width="1.6"><circle cx="12" cy="12" r="10"/><ellipse cx="12" cy="12" rx="4.5" ry="10"/><path d="M2 12h20M4 6.5h16M4 17.5h16"/></svg>
      admin@kqt.com<br>kqt.com
    </div>
  </div>
</div>
</body>
</html>
```